Brenwick Drilling Inc. Business card design

Business card design for "Brenwick Drilling Inc. - Directional Drilling Services"

Address is:

Brenwick Drilling Inc.
512 - 73 Tolvane Crescent SW
Calgary, Alberta, Canada
T2K 4P8

Please incorporate the logo design into the card, thank you.

Target Market(s)

Oil & Gas and Drilling

Industry/Entity Type

Business

```html
<!DOCTYPE html>
<html lang="en">
<head>
<meta charset="utf-8">
<title>Brenwick Drilling Inc. – Business Card</title>
<link rel="stylesheet" href="https://fonts.googleapis.com/css2?family=Questrial&family=Tinos&display=swap">
<style>
  :root {
    --canvas-bg: #f1f1f3;
    --card-white: #ffffff;
    --card-black: #000000;
    --brand-navy: #2e3192;
    --brand-sky: #00a9e6;
    --back-text: #ffffff;
    --back-glow: rgba(255, 255, 255, 0.55);
  }

  html, body {
    margin: 0;
    padding: 0;
    overflow: hidden;
  }

  .canvas {
    position: relative;
    width: 848px;
    height: 1200px;
    background: var(--canvas-bg);
    overflow: hidden;
  }

  .card {
    position: absolute;
    left: 144px;
    width: 560px;
    height: 326px;
    box-shadow: 0 2px 6px rgba(0, 0, 0, 0.12);
  }

  .card--front {
    top: 200px;
    background: var(--card-white);
  }

  .card--back {
    top: 660px;
    background: var(--card-black);
    display: flex;
    align-items: center;
    justify-content: center;
  }

  .company-name {
    position: absolute;
    left: 0;
    right: 0;
    top: 160px;
    margin: 0;
    text-align: center;
    font-family: "Questrial", sans-serif;
    font-size: 30px;
    font-weight: 400;
    letter-spacing: 0.2px;
    color: var(--brand-navy);
  }

  .accent-band {
    position: absolute;
    left: 0;
    bottom: 0;
    width: 560px;
    height: 22px;
    display: block;
  }

  .band-navy { fill: var(--brand-navy); }
  .band-sky { fill: var(--brand-sky); }

  .service-line {
    margin: 0;
    font-family: "Tinos", serif;
    font-size: 22px;
    color: var(--back-text);
    text-shadow: 0 0 4px var(--back-glow), 0 0 10px var(--back-glow);
  }
</style>
</head>
<body>
  <main class="canvas">
    <section class="card card--front" aria-label="Card front">
      <h1 class="company-name">Brenwick Drilling Inc.</h1>
      <svg class="accent-band" viewBox="0 0 560 22" aria-hidden="true">
        <polygon class="band-navy" points="0,0 292,0 272,22 0,22"/>
        <polygon class="band-sky" points="302,0 560,0 560,22 282,22"/>
      </svg>
    </section>

    <section class="card card--back" aria-label="Card back">
      <p class="service-line">Directional Drilling Services</p>
    </section>
  </main>
</body>
</html>
```